3D Printing Business coming soon page

Hi we are looking for a one page "coming soon" website for our business. The business is called "Solevia Labs" and it is a new solution which 3D Prints Orthotics (Insoles).

The design should include our logo, an improved version of our promotional image (attached), a web form for capturing interest from people, a countdown timer and some text.

Follow the colour scheme which is shown in our logo along with our other colours - Orange (RGB#ff8300) and Light Green (RGB#30f20a)
Updates

Industry/Entity Type

Business

Font styles to use
Sans Serif

Requirements
Must have
• Logo (Attached)
Improved version of Promotional Image
Web Form design for capturing Name, EMail Address and Comments along with a Turin test
Countdown Timer
Text - "Solevia Labs will shake up the Orthotics Industry. Foot Orthosis patient-ready in hours for a fraction of the price you are paying today. Welcome to the new world of 3D Printing!"

```html
<!DOCTYPE html>
<html lang="en">
<head>
<meta charset="utf-8">
<title>Solevia Labs – Coming Soon</title>
<link href="https://fonts.googleapis.com/css2?family=Arimo:wght@400;700&family=Roboto+Condensed:wght@400&display=swap" rel="stylesheet">
<style>
  :root {
    --green: #5cff00;
    --orange: #ff6a00;
    --orange-text: #ff6a12;
    --navy: #0b3a94;
    --sky: #3bbcf2;
    --royal: #1a2fd0;
    --white: #ffffff;
    --ink: #1a1a1a;
    --grey-dark: #3c3c3c;
    --grey-light: #9a9a9a;
  }
  * { box-sizing: border-box; margin: 0; padding: 0; }
  html, body { width: 1200px; height: 1000px; overflow: hidden; background: var(--white); }
  body { position: relative; font-family: "Arimo", Arial, sans-serif; }
  .abs { position: absolute; }

  /* Header */
  .header { left: 280px; top: 0; width: 640px; height: 155px; background: var(--green); }
  .brand-mark { left: 40px; top: 18px; width: 118px; height: 118px; border-radius: 50%; background: var(--navy); }
  .brand-name { left: 236px; top: 30px; font-size: 30px; letter-spacing: 5px; color: var(--royal); }
  .brand-tagline { left: 234px; top: 88px; font-size: 32px; letter-spacing: 5px; color: var(--white); }

  /* Countdown */
  .countdown { left: 280px; top: 180px; width: 640px; height: 60px; background: var(--navy); color: var(--white); font-weight: 700; }
  .countdown-label { left: 37px; top: 22px; font-size: 16px; letter-spacing: 1px; }
  .countdown-box { left: 300px; top: 16px; width: 115px; height: 28px; background: var(--white); border-radius: 6px; box-shadow: 2px 4px 4px rgba(0,0,0,.6), 0 0 0 2px #5c7fd0; }
  .countdown-unit { left: 455px; top: 21px; font-size: 16px; }

  .headline { left: 280px; top: 265px; width: 640px; text-align: center; font-size: 21px; letter-spacing: 2.5px; color: var(--orange-text); }

  /* Promo */
  .promo { left: 280px; top: 311px; width: 640px; height: 309px; background: linear-gradient(90deg, var(--navy) 0%, var(--navy) 25%, var(--sky) 55%, var(--sky) 100%); overflow: hidden; }
  .promo-lead { left: 0; top: 11px; width: 640px; text-align: center; font-family: "Roboto Condensed", "Arial Narrow", sans-serif; font-size: 18px; color: var(--white); }
  .steps { left: -2px; top: 47px; width: 644px; height: 49px; border: 2px solid var(--orange); border-radius: 3px; background: linear-gradient(90deg, var(--sky) 0%, var(--navy) 25%, var(--navy) 100%); }
  .step { top: 11px; font-family: "Roboto Condensed", "Arial Narrow", sans-serif; font-size: 19px; color: var(--white); letter-spacing: .5px; }
  .step-tab { top: 93px; width: 40px; height: 5px; background: var(--green); border-radius: 0 0 4px 4px; box-shadow: 2px 2px 2px rgba(0,0,0,.5); }
  .step-visual { top: 128px; height: 122px; border-radius: 6px; }
  .visual-scan { left: 15px; width: 118px; background: linear-gradient(135deg, #ececec, #a9a9a9); }
  .visual-design { left: 162px; top: 142px; width: 153px; height: 83px; background: linear-gradient(90deg, #f4f4f4, #e8c3c0); }
  .visual-print { left: 372px; top: 136px; width: 94px; height: 96px; background: linear-gradient(180deg, #b0486e, #e6eef4); }
  .visual-fit { left: 523px; top: 146px; width: 102px; height: 58px; background: linear-gradient(90deg, #2a2a2a, #c9a98a); }
  .promo-foot { left: 0; top: 262px; width: 640px; height: 47px; border-top: 4px solid #9fdcf8; background: linear-gradient(90deg, var(--navy) 0%, var(--navy) 60%, var(--sky) 85%); }
  .promo-foot-text { left: 0; top: 10px; width: 640px; text-align: center; font-family: "Roboto Condensed", "Arial Narrow", sans-serif; font-size: 22px; color: var(--white); }

  /* Forms */
  .forms { left: 280px; top: 658px; width: 640px; height: 298px; background: var(--orange); }
  .form-title { top: 13px; font-size: 15px; font-weight: 700; letter-spacing: 1px; color: var(--white); }
  .form-panel { top: 31px; width: 242px; height: 256px; background: var(--green); border-radius: 9px; }
  .field-label { font-family: "Roboto Condensed", "Arial Narrow", sans-serif; font-size: 14px; color: var(--white); }
  .field { background: var(--white); border: 2px solid var(--ink); border-radius: 6px; height: 23px; width: 153px; }
  .btn { top: 226px; width: 56px; height: 19px; border-radius: 5px; font-family: "Roboto Condensed", "Arial Narrow", sans-serif; font-size: 14px; text-align: center; line-height: 18px; box-shadow: 2px 2px 2px rgba(0,0,0,.5); }
  .btn-dark { background: linear-gradient(180deg, var(--grey-light), var(--grey-dark) 60%); color: var(--white); }
  .btn-light { background: linear-gradient(180deg, #ffffff 60%, #c8c8c8); color: var(--navy); }
</style>
</head>
<body>
  <header class="abs header">
    <div class="abs brand-mark"></div>
    <div class="abs brand-name">Solevia Labs</div>
    <div class="abs brand-tagline">3D Prints Orthotics</div>
  </header>

  <section class="abs countdown">
    <div class="abs countdown-label">Web page Coming soon</div>
    <div class="abs countdown-box"></div>
    <div class="abs countdown-unit">Days to left</div>
  </section>

  <h1 class="abs headline" style="font-weight:400">Solevia Labs will shake up the Orthotics Industry.</h1>

  <section class="abs promo">
    <p class="abs promo-lead">Foot Orthosis patient-ready in hours for a fraction of the price you are paying today.</p>
    <div class="abs steps"></div>
    <span class="abs step" style="left:13px;top:58px">1. Scan the foot</span>
    <span class="abs step" style="left:156px;top:60px">2. Design the Orthotic</span>
    <span class="abs step" style="left:369px;top:60px">3. 3D Print it</span>
    <span class="abs step" style="left:540px;top:58px">4. Fit it</span>
    <span class="abs step-tab" style="left:51px"></span>
    <span class="abs step-tab" style="left:217px"></span>
    <span class="abs step-tab" style="left:395px"></span>
    <span class="abs step-tab" style="left:546px"></span>
    <div class="abs step-visual visual-scan" role="img" aria-label="Tablet with 3D foot scanner attached"></div>
    <div class="abs step-visual visual-design" role="img" aria-label="Orthotic design software showing a foot and insole model"></div>
    <div class="abs step-visual visual-print" role="img" aria-label="Desktop 3D printer"></div>
    <div class="abs step-visual visual-fit" role="img" aria-label="Hands fitting a printed insole into a shoe"></div>
    <div class="abs promo-foot">
      <p class="abs promo-foot-text">Welcome to the new world of 3D Printing!</p>
    </div>
  </section>

  <section class="abs forms">
    <h2 class="abs form-title" style="left:57px">Turin Test</h2>
    <form class="abs form-panel" style="left:45px">
      <span class="abs field-label" style="left:12px;top:19px">Question 1</span>
      <span class="abs field" style="left:77px;top:17px"></span>
      <span class="abs field-label" style="left:11px;top:63px">Question 2</span>
      <span class="abs field" style="left:76px;top:59px"></span>
      <span class="abs field-label" style="left:11px;top:103px">Question 3</span>
      <span class="abs field" style="left:76px;top:99px"></span>
      <span class="abs field-label" style="left:11px;top:145px">Question 4</span>
      <span class="abs field" style="left:76px;top:141px"></span>
      <span class="abs field-label" style="left:11px;top:186px">Question 5</span>
      <span class="abs field" style="left:77px;top:181px"></span>
      <span class="abs btn btn-dark" style="left:55px">Send</span>
      <span class="abs btn btn-dark" style="left:140px">Quit</span>
    </form>

    <h2 class="abs form-title" style="left:365px">Contact Form</h2>
    <form class="abs form-panel" style="left:351px">
      <span class="abs field-label" style="left:16px;top:16px">Email</span>
      <span class="abs field" style="left:77px;top:17px"></span>
      <span class="abs field-label" style="left:12px;top:56px">Address</span>
      <span class="abs field" style="left:76px;top:58px"></span>
      <span class="abs field-label" style="left:11px;top:102px">Comments</span>
      <span class="abs field" style="left:77px;top:102px;height:106px"></span>
      <span class="abs btn btn-light" style="left:54px">Send</span>
      <span class="abs btn btn-light" style="left:139px;top:224px">Refresh</span>
    </form>
  </section>
</body>
</html>
```